Flyer für Freie Referentin
I thank Merak Tuwero for the great work! I’am very satisfied with the design of my flyer, with the arrangement of the photos, the font and the colors. Everything is fine and exactly as I imagined before. All my requested changings were changed very quickly and correctly. I would definitely recommend this designer!
Zielgruppe
Ich biete Vorträge, Kurse, Fortbildungen und Privatunterricht an zu den Themen:
Einführung in die Weltreligionen
und
Feste der Religionen
Außerdem biete ich Führungen durch religiöse Gebäude in Berlin an.
Meine Zielgruppen sind:
1. Pädagogen in Kita, Grund-und Oberschule,
2. Religionslehrer,
3.Fachkräfte im interkulturellen Kontext (Ausländerbehörde, Gesundheitswesen, Sozialwesen) und
4. Menschen, die gern reisen und sich für andere Religionen und Kulturen interessieren
Aufgabenstellung
Ich habe selbst einen 6 seitigen Falzflyer entworfen, mit Text und Bildern und würde diesen inhaltlich weitgehend so lassen, und nur in einem ansprechenden Design umgestalten lassen. Die Fotos, die ich liefere, habe ich in den religiösen Gebäuden selbst gemacht.

```html
<!DOCTYPE html>
<html lang="de">
<head>
<meta charset="utf-8">
<title>Weltreligionen in Berlin erleben – Falzflyer</title>
<link href="https://fonts.googleapis.com/css2?family=Cinzel:wght@600;700;800&family=Poppins:ital,wght@0,400;0,500;0,600;1,400&display=swap" rel="stylesheet">
<style>
:root{
  --maroon:#8a1a24;
  --maroon-dark:#6e1119;
  --gold:#f5b624;
  --mustard:#d8b24c;
  --ink:#0e0e0e;
  --paper:#ecebe9;
  --cream:#f6f3ee;
  --stage:#d7d7d7;
  --white:#ffffff;
  --text:#222222;
}
*{box-sizing:border-box;margin:0;padding:0}
html,body{width:706px;height:1200px;overflow:hidden}
body{background:var(--stage);font-family:"Poppins",sans-serif;color:var(--text);position:relative}
.spread{position:absolute;left:18px;width:670px;height:474px;display:grid;grid-template-columns:repeat(3,1fr);box-shadow:0 6px 18px rgba(0,0,0,.18)}
.spread--outside{top:96px}
.spread--inside{top:626px}
.panel{position:relative;overflow:hidden}
.cinzel{font-family:"Cinzel",serif;font-weight:700}
.photo{position:absolute}
.ticks{list-style:none}
.ticks li{position:relative;padding-left:14px}
.ticks li::before{content:"";position:absolute;left:2px;top:1px;width:3px;height:6px;border-right:2px solid var(--gold);border-bottom:2px solid var(--gold);transform:rotate(45deg)}
.ticks--dark li::before{border-color:var(--maroon)}
.ticks--white li::before{border-color:var(--white)}
.rule{height:1px;background:var(--maroon)}

/* outside – about */
.about{background:var(--maroon)}
.about__top{position:absolute;inset:0 0 auto 0;height:280px;background:var(--gold)}
.about__title{position:absolute;top:16px;left:0;right:0;text-align:center;font-size:11px;color:var(--maroon)}
.about__rule{position:absolute;top:34px;left:12px;right:12px}
.about__photo{left:0;right:0;top:42px;height:232px;background:radial-gradient(ellipse at 50% 55%,#e9a032 0%,#f0aa2a 45%,#f5b624 100%)}
.about__wave{position:absolute;left:0;top:256px;width:100%;height:30px}
.about__name{position:absolute;top:290px;left:0;right:0;text-align:center;font-size:15px;color:var(--white)}
.about__list{position:absolute;top:318px;left:28px;right:16px;color:var(--white);font-size:7px;line-height:1.3}
.about__list li{margin-bottom:9px}
.bottom-stripe{position:absolute;left:0;right:0;bottom:0;height:5px;background:var(--gold)}

/* outside – contact */
.contact{background:var(--paper)}
.contact__corner{position:absolute;top:0;left:0;width:100%;height:60px}
.contact__box{position:absolute;top:18px;left:16px;right:16px;height:198px;background:var(--ink);border-radius:12px;color:var(--white);padding:12px 14px}
.contact__label{text-align:center;font-size:10px;padding-bottom:4px;border-bottom:1px solid var(--white);margin:0 6px}
.contact__name{font-size:15px;color:var(--gold);text-align:center;margin-top:8px;white-space:nowrap}
.contact__role{font-size:6.6px;font-style:italic;text-align:center;margin-bottom:8px}
.contact__line{display:flex;align-items:flex-start;gap:7px;font-size:9.6px;font-weight:600;line-height:1.25;margin-bottom:4px}
.contact__line svg{flex:none;width:9px;height:10px;margin-top:2px}
.contact__symbols{left:56px;right:56px;top:230px;height:86px;background:linear-gradient(180deg,#d9d8d6,#cfcecc);border-radius:6px}
.contact__band{position:absolute;top:330px;left:16px;right:16px;height:19px;background:var(--maroon);color:var(--white);font-size:10.5px;text-align:center;line-height:19px}
.contact__text{position:absolute;top:357px;left:18px;right:12px;font-size:7px;line-height:1.3}
.contact__text p{margin-bottom:7px}
.contact__text li{margin-bottom:7px}

/* outside – cover */
.cover{background:var(--mustard)}
.cover__top{position:absolute;inset:0 0 auto 0;height:136px;background:linear-gradient(160deg,var(--maroon-dark),var(--maroon))}
.cover__title{position:absolute;top:18px;left:0;right:0;text-align:center;color:var(--white);font-size:14px;line-height:1.1}
.cover__div{position:absolute;left:16px;right:16px;height:1px;background:var(--gold)}
.cover__dot{position:absolute;left:50%;width:7px;height:7px;margin-left:-3.5px;border-radius:50%;background:var(--gold)}
.cover__sub{position:absolute;left:0;right:0;text-align:center;color:var(--white);font-size:7.5px;font-weight:500;letter-spacing:.3px;line-height:1.15}
.cover__wave{position:absolute;left:0;top:112px;width:100%;height:36px}
.cover__grid{position:absolute;top:138px;left:0;right:0;height:238px;display:grid;grid-template-columns:1fr 1fr;grid-template-rows:1fr 1fr;gap:2px}
.cover__grid div{position:relative}
.ph-a{background:linear-gradient(135deg,#5a5d66,#c8c4be)}
.ph-b{background:linear-gradient(135deg,#3f7f86,#c98f8a)}
.ph-c{background:linear-gradient(135deg,#d9751e,#9a4d2a)}
.ph-d{background:linear-gradient(135deg,#5d7b3d,#e3e0d8)}
.cover__faiths{position:absolute;top:338px;left:14px;right:14px;height:54px;background:var(--ink);border-radius:6px;color:var(--white);text-align:center;font-size:9.5px;font-weight:500;line-height:1.2;padding-top:6px;letter-spacing:.3px}
.cover__claim{position:absolute;top:405px;left:6px;right:6px;text-align:center;font-size:12.2px;line-height:1.15;color:var(--ink)}

/* inside – offer */
.offer{background:var(--paper)}
.offer__title{position:absolute;top:20px;left:12px;right:12px;text-align:center;font-size:11.5px;line-height:1.02;color:var(--maroon)}
.offer__rule{position:absolute;top:76px;left:12px;right:12px}
.offer__list{position:absolute;top:86px;left:26px;right:14px;font-size:7.5px;line-height:1.25}
.offer__list li{margin-bottom:8px}
.offer__photo{left:0;right:0;top:310px;bottom:0;background:linear-gradient(180deg,#7cb3df 0%,#a9cbe6 40%,#b9b6ad 70%,#4f6a3b 100%)}
.themes{position:absolute;top:214px;left:16px;right:16px;height:152px;background:var(--ink);border-radius:10px;color:var(--white);padding:10px 14px}
.themes__title{font-size:10.5px;line-height:1.05;padding-bottom:6px;border-bottom:1px solid var(--white);margin-bottom:8px}
.themes__head{display:flex;align-items:center;gap:6px;font-size:7.5px;color:var(--gold);margin-bottom:2px}
.num{flex:none;width:11px;height:11px;border-radius:50%;background:var(--gold);color:var(--ink);font-family:"Poppins",sans-serif;font-size:7px;font-weight:600;text-align:center;line-height:11px}
.themes .ticks{font-size:7.2px;line-height:1.25;margin:0 0 7px 16px}
.themes .ticks li{padding-left:11px}

/* inside – visits */
.visits{background:var(--maroon)}
.visits__photo{left:0;right:0;top:0;height:216px;background:linear-gradient(160deg,#3f7a3a 0%,#c8a35a 35%,#b24a2a 60%,#6a6c3e 100%)}
.visits__wave{position:absolute;left:0;top:196px;width:100%;height:30px}
.visits__head{position:absolute;left:12px;right:12px;text-align:center;color:var(--white);font-size:10px}
.visits__rule{position:absolute;left:12px;right:12px;height:1px;background:var(--white)}
.visits__list{position:absolute;left:32px;right:14px;color:var(--white);font-size:7.5px;line-height:1.3}

/* inside – audience */
.audience{background:var(--cream)}
.audience__title{position:absolute;top:22px;left:10px;right:10px;text-align:center;font-size:11px;line-height:1.05;color:var(--maroon)}
.audience__rule{position:absolute;top:54px;left:12px;right:12px}
.audience__list{position:absolute;top:64px;left:18px;right:10px;list-style:none}
.audience__item{display:flex;gap:7px;margin-bottom:9px}
.audience__item .num{background:var(--maroon);color:var(--white);margin-top:1px}
.audience__head{font-size:7.3px;color:var(--maroon);line-height:1.1;margin-bottom:2px}
.audience__item .ticks{font-size:7px;line-height:1.25}
.audience__item .ticks li{padding-left:11px}
.audience__photo{left:0;right:0;top:300px;bottom:0;background:linear-gradient(140deg,#2f6b3a 0%,#d98a1e 40%,#c2502a 60%,#3c7a45 100%)}
.audience__wave{position:absolute;left:0;top:290px;width:100%;height:24px}
</style>
</head>
<body>

<!-- Außenseite -->
<section class="spread spread--outside">

  <article class="panel about">
    <div class="about__top"></div>
    <h2 class="about__title cinzel">Über mich:</h2>
    <div class="about__rule rule"></div>
    <div class="photo about__photo" role="img" aria-label="Porträtfoto der Referentin vor orangefarbenem Hintergrund"></div>
    <svg class="about__wave" viewBox="0 0 223 30" preserveAspectRatio="none"><path d="M0 30 L0 18 Q112 0 223 12 L223 30 Z" fill="#f6f3ee"/><path d="M0 30 L0 22 Q112 4 223 16 L223 30 Z" fill="#8a1a24"/></svg>
    <h1 class="about__name cinzel">Dr. Fenja Morhart</h1>
    <ul class="about__list ticks">
      <li>1992-1999 Studium der Religionswissenschaft und Indologie in Berlin</li>
      <li>2008 Dissertation: „Hindus in der deutschen Diaspora.“</li>
      <li>Seit 2000 Wissenschaftliche Referentin für Weltreligionen und Hinduismus</li>
      <li>Seit 2002 Freie Autorin, Schwerpunkt: Religiöse Gruppen in der Diaspora</li>
    </ul>
    <div class="bottom-stripe"></div>
  </article>

  <article class="panel contact">
    <svg class="contact__corner" viewBox="0 0 223 60" preserveAspectRatio="none"><path d="M0 0 L223 0 L223 10 Q120 14 30 60 L0 60 Z" fill="#8a1a24"/><path d="M0 0 L12 0 L34 22 L0 60 Z" fill="#f5b624"/></svg>
    <div class="contact__box">
      <div class="contact__label cinzel">Kontakt</div>
      <div class="contact__name cinzel">Dr. Fenja Morhart</div>
      <div class="contact__role">Religionswissenschaftlerin und Indologin</div>
      <div class="contact__line"><svg viewBox="0 0 10 12"><path d="M5 0a4 4 0 0 0-4 4c0 3 4 8 4 8s4-5 4-8a4 4 0 0 0-4-4zm0 5.6a1.6 1.6 0 1 1 0-3.2 1.6 1.6 0 0 1 0 3.2z" fill="#f5b624"/></svg><span>Lindenhofweg 8<br>10115 Berlin</span></div>
      <div class="contact__line"><svg viewBox="0 0 10 10"><circle cx="5" cy="5" r="5" fill="#f5b624"/><path d="M3 2.5l1 1-.6.8c.4.8 1 1.4 1.8 1.8l.8-.6 1 1-.7.9C4.6 7.2 2.8 5.4 2.6 3.2z" fill="#0e0e0e"/></svg><span>030 55501234</span></div>
      <div class="contact__line"><svg viewBox="0 0 8 12"><rect x="1" y="0.5" width="6" height="11" rx="1" fill="none" stroke="#f5b624" stroke-width="1.2"/><rect x="3" y="9" width="2" height="1" fill="#f5b624"/></svg><span>0176 55508821</span></div>
      <div class="contact__line"><svg viewBox="0 0 10 10"><circle cx="5" cy="5" r="5" fill="#f5b624"/><rect x="2.3" y="3.2" width="5.4" height="3.6" fill="none" stroke="#0e0e0e" stroke-width=".8"/><path d="M2.3 3.2L5 5.3l2.7-2.1" fill="none" stroke="#0e0e0e" stroke-width=".8"/></svg><span>info@fermoxa.de</span></div>
      <div class="contact__line"><svg viewBox="0 0 10 10"><circle cx="5" cy="5" r="5" fill="#f5b624"/><circle cx="5" cy="5" r="2.8" fill="none" stroke="#0e0e0e" stroke-width=".7"/><path d="M2.2 5h5.6M5 2.2v5.6" stroke="#0e0e0e" stroke-width=".7"/></svg><span>www.fermoxa.de</span></div>
    </div>
    <div class="photo contact__symbols" role="img" aria-label="Symbole der fünf Weltreligionen"></div>
    <h3 class="contact__band cinzel">Mehr Infos &amp; Buchung</h3>
    <div class="contact__text">
      <p>Ich biete Seminare für Einzelpersonen, Bildungseinrichtungen und Teams an – in meinem Büro oder vor Ort.</p>
      <ul class="ticks ticks--dark">
        <li>Aktuelle Preise und Konditionen finden Sie auf meiner Website www.fermoxa.de</li>
        <li>Individuelle Angebote – Preise auf Nachfrage unter: info@fermoxa.de oder: Tel.: 03(0) 55501 234</li>
      </ul>
    </div>
    <div class="bottom-stripe"></div>
  </article>

  <article class="panel cover">
    <div class="cover__top"></div>
    <h2 class="cover__title cinzel">Weltreligionen in<br>Berlin erleben</h2>
    <div class="cover__div" style="top:60px"></div><span class="cover__dot" style="top:56.5px"></span>
    <p class="cover__sub" style="top:70px">VORTRÄGE &amp; SEMINARE</p>
    <div class="cover__div" style="top:84px"></div><span class="cover__dot" style="top:80.5px"></span>
    <p class="cover__sub" style="top:92px">FÜHRUNGEN &amp; PRIVATUNTERRICHT<br>IN BERLIN</p>
    <svg class="cover__wave" viewBox="0 0 223 36" preserveAspectRatio="none"><path d="M0 6 Q112 30 223 18 L223 36 L0 36 Z" fill="#f5b624"/><path d="M0 14 Q112 36 223 26 L223 36 L0 36 Z" fill="#d8b24c"/></svg>
    <div class="cover__grid">
      <div class="ph-a" role="img" aria-label="Foto: jüdischer Gläubiger mit Gebetsschal"></div>
      <div class="ph-b" role="img" aria-label="Foto: muslimische Frauen bei einer Feier"></div>
      <div class="ph-c" role="img" aria-label="Foto: buddhistische Mönche in orangefarbenen Gewändern"></div>
      <div class="ph-d" role="img" aria-label="Foto: christliche Prozession in weißen Gewändern"></div>
    </div>
    <div class="cover__faiths">JUDENTUM | CHRISTENTUM |<br>ISLAM | HINDUISMUS |<br>BUDDHISMUS</div>
    <h2 class="cover__claim cinzel">Lernen Sie die<br>Weltreligionen kennen<br>und verstehen!</h2>
  </article>
</section>

<!-- Innenseite -->
<section class="spread spread--inside">

  <article class="panel offer">
    <h2 class="offer__title cinzel">Weltreligionen verstehen – Menschen besser begegnen Mein Angebot:</h2>
    <div class="offer__rule rule"></div>
    <ul class="offer__list ticks ticks--dark">
      <li>Vorträge &amp; Seminare zu: Judentum, Christentum, Islam, Hinduismus und Buddhismus</li>
      <li>Vorträge &amp; Seminare zu religiösen Festen und Traditionen</li>
      <li>Besuche religiöser Stätten</li>
      <li>Individuelle Weiterbildungen &amp; Privatunterricht</li>
    </ul>
    <div class="photo offer__photo" role="img" aria-label="Foto: Moschee mit Kuppel unter blauem Himmel"></div>
    <div class="themes">
      <h3 class="themes__title cinzel">Welche Themen biete ich an?</h3>
      <div class="themes__head cinzel"><span class="num">1</span>Einführung Weltreligionen</div>
      <ul class="ticks ticks--white"><li>Ursprung &amp; Heilige Schrift</li><li>Lehren &amp; Rituale</li><li>Ethik &amp; Verhalten</li></ul>
      <div class="themes__head cinzel"><span class="num">2</span>Feste in den Religionen</div>
      <ul class="ticks ticks--white"><li>Kalender &amp; Anlässe</li><li>Geschichten &amp; Musik</li><li>Rituale &amp; Speisen</li></ul>
    </div>
  </article>

  <article class="panel visits">
    <div class="photo visits__photo" role="img" aria-label="Foto: farbenfrohe hinduistische Straßenprozession"></div>
    <svg class="visits__wave" viewBox="0 0 223 30" preserveAspectRatio="none"><path d="M0 12 Q112 28 223 6 L223 30 L0 30 Z" fill="#f6f3ee"/><path d="M0 16 Q112 32 223 10 L223 30 L0 30 Z" fill="#8a1a24"/></svg>
    <h3 class="visits__head cinzel" style="top:240px">Besuche religiöser Stätten</h3>
    <div class="visits__rule" style="top:256px"></div>
    <ul class="visits__list ticks" style="top:266px"><li>Führung durch die Räume</li><li>Teilnahme an Zeremonien</li><li>Austausch mit Gläubigen</li></ul>
    <h3 class="visits__head cinzel" style="top:330px">Was Sie mitnehmen:</h3>
    <div class="visits__rule" style="top:346px"></div>
    <ul class="visits__list ticks" style="top:356px">
      <li style="margin-bottom:8px">Klar verständliches Wissen zu den Weltreligionen</li>
      <li style="margin-bottom:8px">Hintergründe zu Festen, Bräuchen und Symbolen</li>
      <li>Aha-Momente für Beruf, Alltag und Reisen</li>
    </ul>
  </article>

  <article class="panel audience">
    <h2 class="audience__title cinzel">Meine Angebote richten sich an:</h2>
    <div class="audience__rule rule"></div>
    <ol class="audience__list">
      <li class="audience__item"><span class="num">1</span><div><div class="audience__head cinzel">Lehrkräfte allgemein:</div><ul class="ticks ticks--dark"><li>Gewinnen Sie fundiertes Wissen, um <b>Schüler*innen unterschiedlicher Herkunft</b> besser zu begleiten</li></ul></div></li>
      <li class="audience__item"><span class="num">2</span><div><div class="audience__head cinzel">Religionslehrerinnen und Religionslehrer:</div><ul class="ticks ticks--dark"><li>Vertiefen Sie Ihr Wissen zu Inhalten der großen Religionen – praxisnah und aktuell!</li></ul></div></li>
      <li class="audience__item"><span class="num">3</span><div><div class="audience__head cinzel">Fachkräfte im interkulturellen Kontext (Ausländerbehörde, Asylberatung, Gesundheitswesen)</div><ul class="ticks ticks--dark"><li>Gewinnen Sie Sicherheit im Umgang mit religiös geprägten Verhaltensweisen!</li></ul></div></li>
      <li class="audience__item"><span class="num">4</span><div><div class="audience__head cinzel">Reisefreudige &amp; Neugierige:</div><ul class="ticks ticks--dark"><li>Entdecken Sie spannende Einblicke in Rituale, Werte und Feiertage weltweit!</li></ul></div></li>
    </ol>
    <div class="photo audience__photo" role="img" aria-label="Foto: Hände halten eine Tonschale mit Feuer bei einem Ritual"></div>
    <svg class="audience__wave" viewBox="0 0 223 24" preserveAspectRatio="none"><path d="M0 0 L223 0 L223 6 Q112 22 0 10 Z" fill="#f6f3ee"/></svg>
  </article>
</section>

</body>
</html>
```